Buch-Cover für Berater, Coach und Trainer
Ich habe das erste Mal Ihre Leistung in Anspruch genommen und bin restlos zufrieden. Schön, wenn sich die Entscheidung für einen bestimmten Designer, auch hinterher als absolut richtig herausstellt. Es hätte nicht besser laufen können mit tv studio. Vielen Dank nochmals für die gute Kommunikation und Ihre professionellen Vorschläge.
Zielgruppe
Guten Tag,
ich bin Berater, Coach und Trainer und es geht um die Vermarktung meines (Sach-)Buches 'Deal Sprints'.
Titel des Buches:
Deal Sprints
Untertitel:
Das Upgrade für Ihre Verkaufskompetenz
Zielgruppe:
Verkäufer oder Menschen, die andere für ihre Ideen gewinnen möchten
Bitte melden Sie sich gerne bei Fragen.
Herzliche Grüße
Torsten Wehmeyer
Aufgabenstellung
Das das Buch recht modern geschrieben ist, sollte der Stil schon auch dem Inhalt entsprechen.
Der Titel muss kein Bild haben, gerne auch eine Illustration oder nur Text.
Als Dateiupload lege ich Ihnen den Klappentext bei.

```html
<!DOCTYPE html>
<html lang="de">
<head>
<meta charset="utf-8">
<title>Deal Sprints – Buchumschlag</title>
<link href="https://fonts.googleapis.com/css2?family=Barlow+Semi+Condensed:wght@400;500;700;800&family=Barlow:wght@400;500;700&display=swap" rel="stylesheet">
<style>
  :root {
    --paper: #ffffff;
    --back-green: #5fa18e;
    --spine-green: #a9c5bb;
    --front-dark: #579683;
    --front-light: #67ae99;
    --floor-green: #43907a;
    --edge-blue: #2f9ccf;
    --ink-white: #ffffff;
  }
  * { margin: 0; padding: 0; box-sizing: border-box; }
  html, body {
    width: 1200px; height: 849px; overflow: hidden;
    background: var(--paper);
  }
  .wrap { position: relative; width: 1200px; height: 849px; }

  .back-cover {
    position: absolute; left: 159px; top: 124px; width: 415px; height: 589px;
    background: var(--back-green);
    border: 1px solid var(--edge-blue);
    color: var(--ink-white);
    font-family: "Barlow", sans-serif;
  }
  .back-title {
    position: absolute; left: 28px; top: 58px;
    font-family: "Barlow Semi Condensed", sans-serif;
    font-weight: 700; font-size: 31px; letter-spacing: 1.5px; line-height: 1;
  }
  .blurb {
    position: absolute; left: 28px; top: 98px; width: 362px;
    font-size: 10.6px; line-height: 14.9px; font-weight: 500;
  }
  .blurb p + p { margin-top: 14.9px; }

  .spine {
    position: absolute; left: 574px; top: 124px; width: 54px; height: 589px;
    background: var(--spine-green);
    color: var(--ink-white);
    font-family: "Barlow Semi Condensed", sans-serif; font-weight: 500;
  }
  .spine-text {
    position: absolute; left: 50%;
    transform: translateX(-50%) rotate(-90deg);
    white-space: nowrap; font-size: 17px; letter-spacing: 1.5px;
  }
  .spine-title { top: 140px; }
  .spine-author { top: 488px; }

  .front-cover {
    position: absolute; left: 628px; top: 124px; width: 415px; height: 589px;
    background: radial-gradient(ellipse at 50% 70%, var(--front-light) 0%, var(--front-dark) 80%);
    color: var(--ink-white); overflow: hidden;
  }
  .front-title {
    position: absolute; left: 0; width: 100%; text-align: center;
    font-family: "Barlow Semi Condensed", sans-serif; font-weight: 800;
    line-height: 1;
  }
  .title-top { top: 56px; font-size: 108px; letter-spacing: 1px; }
  .title-bottom { top: 156px; font-size: 102px; letter-spacing: 0; }
  .subtitle-band {
    position: absolute; left: 0; top: 198px; width: 100%; height: 28px;
    background: #5d9f8b;
    display: flex; align-items: center; justify-content: center;
    font-family: "Barlow Semi Condensed", sans-serif; font-weight: 500;
    font-size: 16.5px; letter-spacing: 0.3px;
  }
  .illustration {
    position: absolute; left: 20px; top: 286px; width: 375px; height: 240px;
    background: radial-gradient(ellipse at 50% 45%, #85bfae 0%, #6aaf9a 45%, rgba(103,174,153,0) 75%);
    border-radius: 50% 50% 10px 10px;
  }
  .floor {
    position: absolute; left: 0; top: 524px; width: 100%; height: 65px;
    background: var(--floor-green);
  }
  .front-author {
    position: absolute; left: 0; top: 548px; width: 100%; text-align: center;
    font-family: "Barlow Semi Condensed", sans-serif; font-weight: 500;
    font-size: 21px; letter-spacing: 1px;
  }
</style>
</head>
<body>
<div class="wrap">
  <section class="back-cover">
    <h2 class="back-title">DEAL SPRINTS</h2>
    <div class="blurb">
      <p>Lorem ipsum dolor sit amet, consectetuer adipiscing elit, sed diam nonummy nibh euismod tincidunt ut laoreet dolore magna aliquam erat volutpat. Ut wisi enim ad minim veniam, quis nostrud exerci tation ullamcorper suscipit lobortis nisl ut aliquip ex ea commodo consequat. Duis autem vel eum iriure dolor in hendrerit in vulputate velit esse molestie consequat, vel illum dolore eu feugiat nulla facilisis at vero et accumsan et iusto odio dignissim qui blandit praesent luptatum zzril delenit augue</p>
      <p>duis dolore te feugait nulla facilisi. Lorem ipsum dolor sit amet, consectetuer adipiscing elit, sed diam nonummy nibh euismod tincidunt ut laoreet dolore magna aliquam erat volutpat. Ut wisi enim ad minim veniam, quis nostrud exerci tation ullamcorper suscipit lobortis nisl ut aliquip ex ea commodo consequat. Duis autem vel eum iriure dolor in hendrerit in vulputate velit esse molestie consequat, vel illum dolore eu</p>
      <p>feugiat nulla facilisis at vero et accumsan et iusto odio dignissim qui blandit praesent luptatum zzril delenit augue duis dolore te feugait nulla facilisi. Nam liber tempor cum soluta nobis eleifend option congue nihil imperdiet doming id quod mazim placerat facer possim assum.</p>
    </div>
  </section>

  <section class="spine">
    <span class="spine-text spine-title">DEAL SPRINTS</span>
    <span class="spine-text spine-author">TORSTEN WEHMEYER</span>
  </section>

  <section class="front-cover">
    <div class="floor"></div>
    <div class="illustration" role="img" aria-label="Illustration: zwei Geschäftsleute in Anzügen schieben zwei Gehirnhälften zusammen, umgeben von gepunkteten Kreisen"></div>
    <h1 class="front-title title-top">DEAL</h1>
    <div class="front-title title-bottom">SPRINTS</div>
    <div class="subtitle-band">DAS UPGRADE FÜR IHRE VERKAUFSKOMPETENZ</div>
    <div class="front-author">TORSTEN WEHMEYER</div>
  </section>
</div>
</body>
</html>
```